Business Card Design

Please visit www.RobHartwell.com to acquire information for business card.

Back Side of Card:
a lifetime of experience working for you.

With over 25 years in the construction industry, well over a decade as a licensed Subcontractor / General Contractor and nearly 10 years as a licensed Realtor, I have excelled and cultivated a working knowledge of how all the pieces fit together.

Here is a link to folder.
https://files.examplestore.net/folderview?id=7Kq2XwPmR4tLvN9sBz8yHc3DfGaJ&usp=sharing

Industry/Entity Type

Construction

Contact Information for Business Card

Company: Rob Hartwell, LLC.
Address: 31872 W. Cedar Hollow Blvd. Suite 207-384
Name: Rob Hartwell
Phone: (623) 587-2914
Web: www.RobHartwell.com
Type of services offered: Architectural Design, 3D Models, Renderings & Animation - Construction Documents - Project Managment.

```html
<!DOCTYPE html>
<html lang="en">
<head>
<meta charset="utf-8">
<title>Rob Hartwell, LLC. — Business Card</title>
<link href="https://fonts.googleapis.com/css2?family=Dosis:wght@400;500;600&family=Exo+2:wght@700&display=swap" rel="stylesheet">
<style>
  :root {
    --page-bg: #d9dadd;
    --card-navy: #141633;
    --card-glow: #3a2f86;
    --text-sky: #9fd6f2;
    --text-soft: #c9d6ef;
    --band-start: #5ab7e8;
    --band-end: #dcf1fa;
    --name-ink: #1a1d3d;
    --logo-violet: #8d78d8;
  }
  * { box-sizing: border-box; margin: 0; padding: 0; }
  html, body { width: 1200px; height: 1000px; overflow: hidden; }
  body {
    background: var(--page-bg);
    font-family: "Dosis", sans-serif;
    display: flex;
    flex-direction: column;
    align-items: center;
    justify-content: center;
    gap: 60px;
  }
  .card {
    position: relative;
    width: 700px;
    height: 400px;
    border-radius: 4px;
    overflow: hidden;
    color: var(--text-soft);
    background:
      radial-gradient(ellipse 60% 55% at 55% 55%, var(--card-glow) 0%, transparent 70%),
      var(--card-navy);
    box-shadow: 0 10px 30px rgba(0,0,0,.35);
  }

  /* Back side */
  .card--back { padding: 48px 56px; }
  .back-title {
    font-size: 29px;
    font-weight: 500;
    letter-spacing: 1px;
    color: var(--text-sky);
    text-align: center;
    margin-bottom: 26px;
  }
  .back-copy {
    font-size: 25px;
    line-height: 1.28;
    color: var(--text-sky);
  }

  /* Front side */
  .brand {
    position: absolute;
    left: 48px; top: 34px;
    display: flex;
    align-items: center;
    gap: 18px;
  }
  .brand-mark {
    width: 78px; height: 78px;
    border: 2px solid var(--logo-violet);
  }
  .brand-name {
    font-size: 36px;
    font-weight: 500;
    color: var(--text-sky);
    margin-top: 30px;
  }
  .name-band {
    position: absolute;
    left: 0; right: 0; top: 130px;
    height: 44px;
    background: linear-gradient(90deg, var(--band-start), var(--band-end));
  }
  .person-name {
    position: absolute;
    left: 72px; top: 128px;
    font-family: "Exo 2", sans-serif;
    font-size: 34px;
    font-weight: 700;
    letter-spacing: 2px;
    color: var(--name-ink);
    line-height: 48px;
  }
  .contact {
    position: absolute;
    left: 48px; top: 192px;
    padding-left: 18px;
    border-left: 2px solid var(--text-soft);
    list-style: none;
  }
  .contact li {
    display: flex;
    align-items: center;
    gap: 12px;
    font-size: 20px;
    line-height: 26px;
    color: var(--text-soft);
  }
  .contact svg { width: 20px; height: 20px; flex: none; }
  .services {
    position: absolute;
    left: 0; right: 0; top: 296px;
    text-align: center;
    color: var(--text-soft);
  }
  .services-title {
    font-size: 21px;
    text-decoration: underline;
    text-underline-offset: 4px;
    margin-bottom: 6px;
  }
  .services-list { font-size: 18px; line-height: 22px; }
</style>
</head>
<body>

  <section class="card card--back">
    <h2 class="back-title">A LIFETIME OF EXPERIENCE WORKING FOR YOU.</h2>
    <p class="back-copy">with over 25 years in the construction industry, well over a decade as a licensed Subcontractor/General contractor and nearly 10 years as a licensed Realtor, I have excelled and cultivated a working knowledge of how all the pieces fit together.</p>
  </section>

  <section class="card card--front">
    <div class="brand">
      <div class="brand-mark"></div>
      <span class="brand-name">Rob Hartwell, LLC.</span>
    </div>

    <div class="name-band"></div>
    <h1 class="person-name">Rob Hartwell</h1>

    <ul class="contact">
      <li>
        <svg viewBox="0 0 20 20" fill="none" stroke="currentColor" stroke-width="1.6"><path d="M2 10 L10 3 L18 10"/><path d="M4.5 8.5 V17 H15.5 V8.5"/><rect x="8" y="11" width="4" height="6"/></svg>
        31872 W. Cedar Hollow Blvd. Suite 207-384
      </li>
      <li>
        <svg viewBox="0 0 20 20" fill="none" stroke="currentColor" stroke-width="1.6"><rect x="2" y="2" width="16" height="16" rx="3"/><path d="M7 5 C5 7 6 11 9 13.5 C11 15 13 15.5 14.5 14 L13 12 L11.5 12.8 C10 12 8.5 10.5 7.8 9 L8.7 7.6 Z" fill="currentColor" stroke="none"/></svg>
        (623) 587-2914
      </li>
      <li>
        <svg viewBox="0 0 20 20" fill="none" stroke="currentColor" stroke-width="1.4"><circle cx="10" cy="10" r="8"/><ellipse cx="10" cy="10" rx="3.5" ry="8"/><path d="M2 10 H18 M3.5 6 H16.5 M3.5 14 H16.5"/></svg>
        www.RobHartwell.com
      </li>
    </ul>

    <div class="services">
      <p class="services-title">Type of services offered</p>
      <p class="services-list">Architectural Design • 3D Models • Rendering &amp; Animation<br>Construction Documents • Project Managements</p>
    </div>
  </section>

</body>
</html>
```